Independent Financial Advisor Billboard Campaign - Granite Bridge Financial

I am a local, independent financial advisor. My company is Granite Bridge Financial, located in Charleston, WV. My main source of revenue comes from those nearing or entering retirement that need assistance with financial planning and investment management. Many are looking to rollover their employer retirement plan into an IRA account. I would like a billboard design campaign that focuses on this type of client. Please see our website www.granitebridgefinancial-example.com for more information.

```html
<!DOCTYPE html>
<html lang="en">
<head>
<meta charset="utf-8">
<title>Granite Bridge Financial – Retirement Billboard</title>
<link href="https://fonts.googleapis.com/css2?family=Playfair+Display:wght@700;800&family=Poppins:wght@600;700&family=Cinzel:wght@500&display=swap" rel="stylesheet">
<style>
  :root {
    --stage: #8f8f8f;
    --charcoal: #2a2a2b;
    --charcoal-deep: #1d1d1e;
    --paper: #ffffff;
    --navy: #17447a;
    --ink: #2b2b2b;
    --chart: rgba(255,255,255,0.07);
  }
  * { margin: 0; padding: 0; box-sizing: border-box; }
  html, body { width: 991px; height: 1200px; overflow: hidden; }
  body { background: var(--stage); position: relative; }

  .billboard {
    position: absolute;
    left: 30px; top: 466px;
    width: 931px; height: 268px;
    background: var(--paper);
    overflow: hidden;
    box-shadow: 0 8px 14px rgba(0,0,0,0.35);
  }
  .headline-band {
    position: absolute; left: 0; top: 0;
    width: 719px; height: 159px;
    background: linear-gradient(90deg, var(--charcoal) 0%, var(--charcoal) 55%, var(--charcoal-deep) 100%);
  }
  .market-chart { position: absolute; left: 0; top: 0; width: 719px; height: 159px; }
  .headline {
    position: absolute; left: 31px; top: 18px;
    font-family: "Playfair Display", serif;
    font-weight: 800;
    color: var(--paper);
    font-size: 66px;
    line-height: 59px;
    letter-spacing: 0.5px;
    text-transform: uppercase;
  }
  .lifestyle-photo {
    position: absolute; left: 724px; top: 0;
    width: 207px; height: 268px;
    background: linear-gradient(180deg, var(--navy) 0%, #163d6b 55%, #1c2a3a 100%);
  }
  .advisor-photo {
    position: absolute; left: 640px; top: 20px;
    width: 224px; height: 248px;
    border-radius: 40% 40% 6px 6px / 24% 24% 6px 6px;
    background: linear-gradient(180deg, #d8b59c 0%, #e9e2dd 42%, #f4f4f6 60%, #e6e7ea 100%);
  }
  .brand {
    position: absolute; left: 26px; top: 196px;
    display: flex; align-items: center; gap: 9px;
  }
  .brand-mark { width: 20px; height: 20px; background: var(--navy); flex: none; }
  .brand-name {
    font-family: "Cinzel", serif; font-weight: 500;
    font-size: 14px; color: var(--navy);
    letter-spacing: 0.3px; white-space: nowrap;
  }
  .phone {
    position: absolute; left: 297px; top: 172px;
    display: flex; align-items: center; gap: 4px;
    font-family: "Poppins", sans-serif; font-weight: 700;
    font-size: 38px; line-height: 1; color: var(--ink);
    white-space: nowrap;
  }
  .phone-icon { width: 33px; height: 33px; flex: none; }
  .web-pill {
    position: absolute; left: 293px; top: 218px;
    width: 340px; height: 31px;
    background: var(--navy);
    border-radius: 15px 0 0 15px;
    color: var(--paper);
    font-family: "Poppins", sans-serif; font-weight: 700;
    font-size: 12px; letter-spacing: 0.3px;
    display: flex; align-items: center; justify-content: center;
    white-space: nowrap;
  }
</style>
</head>
<body>
  <div class="billboard">
    <div class="headline-band">
      <svg class="market-chart" viewBox="0 0 719 159" aria-hidden="true">
        <g fill="var(--chart)">
          <rect x="530" y="110" width="8" height="49"/><rect x="544" y="95" width="8" height="64"/>
          <rect x="558" y="120" width="8" height="39"/><rect x="572" y="85" width="8" height="74"/>
          <rect x="586" y="100" width="8" height="59"/><rect x="600" y="70" width="8" height="89"/>
          <rect x="614" y="90" width="8" height="69"/><rect x="628" y="60" width="8" height="99"/>
          <rect x="642" y="78" width="8" height="81"/><rect x="656" y="50" width="8" height="109"/>
          <rect x="670" y="66" width="8" height="93"/><rect x="684" y="40" width="8" height="119"/>
        </g>
        <path d="M430 20 C500 10 540 40 600 25 S680 5 719 12" fill="none" stroke="rgba(255,255,255,0.18)" stroke-width="1"/>
      </svg>
      <h1 class="headline">Retirement<br>Done Right!</h1>
    </div>

    <div class="lifestyle-photo" role="img" aria-label="Retired couple walking together along the shore at dusk"></div>
    <div class="advisor-photo" role="img" aria-label="Portrait of the financial advisor in a white polo shirt"></div>

    <div class="brand">
      <span class="brand-mark"></span>
      <span class="brand-name">Granite Bridge Financial</span>
    </div>

    <div class="phone">
      <svg class="phone-icon" viewBox="0 0 36 36" aria-hidden="true">
        <circle cx="18" cy="18" r="17" fill="var(--navy)"/>
        <path d="M12.5 9.5c1-.6 2-.3 2.5.6l1.6 3c.4.8.2 1.7-.5 2.2l-1.2.9c.9 2 2.6 3.8 4.7 4.8l.9-1.2c.5-.7 1.4-.9 2.2-.5l3 1.6c.9.5 1.2 1.5.6 2.5l-.9 1.4c-.8 1.2-2.3 1.7-3.7 1.2C15.6 24.4 11.6 20.4 10 14.5c-.4-1.4.1-2.9 1.2-3.7z" fill="var(--paper)"/>
      </svg>
      <span>304.555.0142</span>
    </div>

    <div class="web-pill">www.granitebridgefinancial-example.com</div>
  </div>
</body>
</html>
```